Varen Psychiatry (Psychiatry clinic offering cutting edge treatments)

2 sided flyer for new psychiatry practice in Boulder, CO. I want something that looks professional, cutting edge, but also welcoming and friendly. My logo and pictures are attached.

Some of the copy:
Personalized, holistic Psychiatry combined with cutting-edge, evidence-based treatments. Our personalized psychiatry plan includes a bio-psycho-social evaluation, personalized treatment plan, medical evaluation for underlying hormonal and electrolyte abnormalities, and genetic testing (when warranted).

We specialize in treatment-resistant depression and substance abuse. We also treat PTSD, Bipolar Disorder, OCD, anxiety disorders, ADHD, and psychotic disorders.

About Dr. Pim- Dr. Pim served as Chief Resident at the largest private psychiatry hospital in Colorado. While there he won 3 consecutive awards for exceptionally high Psychiatry in service test score (99th percentile). He was a board member of Westfield Psychiatric Guild and helped advocate for better Colorado mental health policy. Dr. Pim is uniquely trained in Ketamine, Transcranial Magnetic Stimulation, and integrative psychiatry.

Target Market(s)

Private pay mental health patients, planning to give out to psychologists and family practice doctors

Industry/Entity Type

Medicine/Psychiatry

Colors
0054AA
0677BA
7BADD7
CADEEF
E8F1F8
0094D4
00A9DD
6FCCEA
C7EBF8
E9F6FB
00AB8E
00BBA5
67D7C9
C6EFE9
E9F9F6

Requirements
Must have
• My logo, an about me (Dr. Tom Pim) section

```html
<!DOCTYPE html>
<html lang="en">
<head>
<meta charset="utf-8">
<title>Varen Psychiatry – Two-Sided Flyer</title>
<link href="https://fonts.googleapis.com/css2?family=Oswald:wght@500;600&family=Open+Sans:wght@400;600;700&display=swap" rel="stylesheet">
<style>
  :root{
    --navy:#2a2a68;
    --navy-deep:#232257;
    --purple:#8a4fae;
    --violet:#6a5bb5;
    --teal:#48c2d8;
    --teal-text:#3bb3cf;
    --ink:#3b3d55;
    --grey-logo:#5d6072;
    --lavender:#eeeef7;
    --page:#ffffff;
    --backdrop:#e6e8ed;
  }
  *{box-sizing:border-box;margin:0;padding:0}
  html,body{width:1200px;height:900px;overflow:hidden}
  body{background:var(--backdrop);font-family:"Open Sans",Arial,sans-serif;color:var(--ink);position:relative}

  .flyer{position:absolute;top:88px;width:560px;height:724px;background:var(--page);display:flex;flex-direction:column;box-shadow:0 6px 18px rgba(30,30,60,.18);overflow:hidden}
  .flyer--front{left:30px}
  .flyer--back{left:610px}

  .masthead{height:72px;display:flex;align-items:center;justify-content:space-between;padding:0 24px 0 26px}
  .brand{display:flex;align-items:center;gap:9px}
  .brand__mark{width:30px;height:30px;border-radius:50%;background:var(--violet)}
  .brand__name{font-family:"Open Sans",Arial,sans-serif;font-weight:600;font-size:17px;letter-spacing:1.5px;text-transform:uppercase;color:var(--grey-logo)}
  .announce{font-family:"Oswald",Arial,sans-serif;font-weight:500;font-size:14px;line-height:1.15;text-transform:uppercase;color:var(--navy);text-align:right}
  .announce__place{color:var(--teal-text)}

  .photo{margin:0 20px 0 26px;border-radius:0 30px 0 0}
  .photo--hero{height:250px;position:relative;background:linear-gradient(100deg,#c9d3e6 0%,#8a86bf 35%,#6a4f9a 62%,#9c6aa8 80%,#5d8fc2 100%)}
  .photo--clinic{height:226px;background:linear-gradient(120deg,#2f5d86 0%,#5f95bf 45%,#9cc3de 70%,#dfe9f2 100%)}

  .hero__claim{position:absolute;left:26px;top:92px;width:150px;font-family:"Oswald",Arial,sans-serif;font-weight:500;font-size:15px;line-height:1.3;text-transform:uppercase;color:var(--navy)}

  .intro{padding:14px 24px 10px 26px;font-size:10.5px;line-height:1.5;color:var(--navy)}

  .conditions{display:flex;height:72px;margin-left:26px;background:linear-gradient(90deg,#5cc7dc 0%,#4a8fcb 40%,#6b63b8 70%,#8e4fae 100%)}
  .condition{flex:1;display:flex;flex-direction:column;align-items:center;justify-content:center;gap:5px;border-right:1px solid rgba(255,255,255,.35);color:#fff;font-size:10px;line-height:1.1;text-align:center}
  .condition:last-child{border-right:none}
  .condition svg{width:24px;height:24px;fill:none;stroke:#fff;stroke-width:1.5}

  .details{flex:1;background:var(--lavender);padding:16px 24px 12px 26px;font-size:8.6px;line-height:1.55;color:var(--navy)}
  .details p+p{margin-top:9px}

  .contact{height:48px;background:var(--navy-deep);border-radius:0 26px 0 0;margin-right:20px;display:flex;align-items:center;justify-content:space-between;padding:0 22px;color:#fff;font-size:10.5px}
  .contact__item{display:flex;align-items:center;gap:6px}
  .contact__item svg{width:12px;height:12px;fill:none;stroke:var(--teal);stroke-width:1.8}

  .mission{height:176px;margin:0 20px 0 26px;background:linear-gradient(90deg,#5cc7dc 0%,#6a7cc2 55%,#8e4fae 100%);padding:16px 22px;color:#fff}
  .mission__title{font-family:"Oswald",Arial,sans-serif;font-weight:500;font-size:14.5px;line-height:1.3;text-transform:uppercase;text-align:center;margin-bottom:12px}
  .mission__text{font-size:9px;line-height:1.55}

  .about{flex:1;background:var(--lavender);padding:18px 24px 10px 26px;display:flex;gap:16px}
  .about__body{flex:1}
  .about__name{font-family:"Oswald",Arial,sans-serif;font-weight:600;font-size:15px;color:var(--navy);margin-bottom:6px;text-transform:uppercase}
  .about__text{font-size:8.6px;line-height:1.55;color:var(--navy)}
  .about__cta{margin-top:12px;font-size:12px;color:var(--teal-text)}
  .about__portrait{width:112px;height:118px;background:linear-gradient(160deg,#d8d8dc,#8f9096);flex-shrink:0}
</style>
</head>
<body>

<article class="flyer flyer--front">
  <header class="masthead">
    <div class="brand"><span class="brand__mark"></span><span class="brand__name">Varen Psychiatry</span></div>
    <p class="announce">Varen Psychiatry is now accepting<br>new patients in <span class="announce__place">Boulder, Colorado!</span></p>
  </header>

  <div class="photo photo--hero" role="img" aria-label="Profile of a calm woman with a glowing digital brain network">
    <h2 class="hero__claim">Specializing in evidence-based, state-of-the-art mental health treatment.</h2>
  </div>

  <p class="intro">We specialize in treating patients with treatment resistant depression and substance abuse disorders who have not responded to other forms of treatment. We believe that by providing comprehensive care, we can help our patients heal both emotionally and physically. We also treat patients with:</p>

  <ul class="conditions" style="list-style:none">
    <li class="condition"><svg viewBox="0 0 24 24"><circle cx="12" cy="12" r="8"/><path d="M8 12h8M12 8v8"/></svg>PTSD</li>
    <li class="condition"><svg viewBox="0 0 24 24"><circle cx="12" cy="10" r="6"/><path d="M9 16v5M15 16v5"/></svg>Bipolar<br>Disorder</li>
    <li class="condition"><svg viewBox="0 0 24 24"><circle cx="10" cy="10" r="6"/><path d="M14.5 14.5L20 20"/></svg>OCD</li>
    <li class="condition"><svg viewBox="0 0 24 24"><circle cx="12" cy="12" r="8"/><circle cx="12" cy="12" r="3"/></svg>Anxiety<br>Disorders</li>
    <li class="condition"><svg viewBox="0 0 24 24"><circle cx="12" cy="9" r="5"/><path d="M7 21c0-4 2-6 5-6s5 2 5 6"/></svg>ADHD</li>
    <li class="condition"><svg viewBox="0 0 24 24"><circle cx="12" cy="11" r="7"/><path d="M9 11h6"/></svg>Psychotic<br>Disorders</li>
  </ul>

  <section class="details">
    <p>We know that mental health is complex and that multiple factors can contribute to the development of mental illness. For this reason, we take an integrative approach that considers the whole person. We understand that each individual has their own unique set of experiences, strengths, and challenges, and we tailor our treatment plans to suit each patient's personal needs.</p>
    <p>Too often, when we think about mental health, we focus on just treating symptoms. If someone is depressed, they might take medication to help them feel better. If someone is anxious, they might see a therapist to help them manage their anxiety.</p>
    <p>While these treatments can be helpful, they only address the symptoms of mental illness. To truly address mental health, it is necessary to treat the root causes. This might involve addressing childhood trauma, unresolved conflict, or feelings of worthlessness. It might also involve developing healthy coping mechanisms and learning how to set boundaries. By treating the root causes of mental illness, we can begin to create lasting change.</p>
  </section>

  <footer class="contact">
    <span class="contact__item"><svg viewBox="0 0 12 12"><path d="M6 11S2 7 2 4.5a4 4 0 0 1 8 0C10 7 6 11 6 11z"/></svg>1840 Cedar Ave. Boulder, CO 80302 #210</span>
    <span class="contact__item"><svg viewBox="0 0 12 12"><path d="M2 1.5h2.5l1 2.5-1.5 1a6 6 0 0 0 3 3l1-1.5 2.5 1V10.5A1 1 0 0 1 9.5 11.5 9 9 0 0 1 .5 2.5a1 1 0 0 1 1-1z"/></svg>303-555-0147</span>
    <span class="contact__item"><svg viewBox="0 0 12 12"><circle cx="6" cy="6" r="5"/><path d="M1 6h10M6 1c2 2 2 8 0 10M6 1c-2 2-2 8 0 10"/></svg>www.varenpsych.com</span>
  </footer>
</article>

<article class="flyer flyer--back">
  <header class="masthead">
    <div class="brand"><span class="brand__mark"></span><span class="brand__name">Varen Psychiatry</span></div>
    <p class="announce">Varen Psychiatry is now accepting<br>new patients in <span class="announce__place">Boulder, Colorado!</span></p>
  </header>

  <div class="photo photo--clinic" role="img" aria-label="Doctor with a stethoscope using a digital screen showing a glowing brain scan"></div>

  <section class="mission">
    <h2 class="mission__title">Specializing in evidence-based, state-of-the-art<br>mental health treatment.</h2>
    <p class="mission__text">Our personalized psychiatry plan includes a bio-psycho-social evaluation, tailored treatment plan, medical evaluation for underlying hormonal and electrolyte abnormalities, and genetic testing (when warranted). Our integrative psychiatry approach combines cutting edge, evidence-based treatments with holistic therapies to provide you with the best possible care. In addition, we also offer Ketamine Assisted Therapy, TMS (Transcranial Magnetic Stimulation), and MAT Treatment for Substance abuse. We pride ourselves on always staying up to date on the latest mental health treatments.</p>
  </section>

  <section class="about">
    <div class="about__body">
      <h3 class="about__name">Dr. Tom Pim</h3>
      <p class="about__text">Dr. Tom Pim is a psychiatrist with years of experience providing compassionate, evidence-based care to patients of all ages. He is uniquely trained in several cutting-edge treatments, including Ketamine, Transcranial Magnetic Stimulation (TMS), and integrative psychiatry. Prior to founding Varen Psychiatry, Dr. Pim served as Chief Resident at the largest private psychiatry hospital in Colorado. While there, he won three consecutive awards for exceptionally high Psychiatry in-service test scores (99th percentile). In addition, he was a board member of the Westfield Psychiatric Guild and helped advocate for better Colorado mental health policy. Thanks to his extensive training and experience, Dr. Pim is able to provide each patient with an individualized treatment plan that brings optimum results.</p>
      <p class="about__cta">Get started with Varen, today!</p>
    </div>
    <div class="about__portrait" role="img" aria-label="Portrait photo of Dr. Tom Pim"></div>
  </section>

  <footer class="contact">
    <span class="contact__item"><svg viewBox="0 0 12 12"><path d="M6 11S2 7 2 4.5a4 4 0 0 1 8 0C10 7 6 11 6 11z"/></svg>1840 Cedar Ave. Boulder, CO 80302 #210</span>
    <span class="contact__item"><svg viewBox="0 0 12 12"><path d="M2 1.5h2.5l1 2.5-1.5 1a6 6 0 0 0 3 3l1-1.5 2.5 1V10.5A1 1 0 0 1 9.5 11.5 9 9 0 0 1 .5 2.5a1 1 0 0 1 1-1z"/></svg>303-555-0147</span>
    <span class="contact__item"><svg viewBox="0 0 12 12"><circle cx="6" cy="6" r="5"/><path d="M1 6h10M6 1c2 2 2 8 0 10M6 1c-2 2-2 8 0 10"/></svg>www.varenpsych.com</span>
  </footer>
</article>

</body>
</html>
```